Business Card Design Project

We are not a new company, but renamed to "Norvanta Kitchens" last year. We specialize in modern high-end cabinetry imports. We would like to communicate a sense of quality and cutting edge technology. Ideally the design would incorporate our logo colors, silver, red and preferably a black, matte background. Though we are open to suggestions.
Logo is attached.
Edit: I have attached rough drafts of the previous cards, this way you will have all necessary content that needs to go on the cards.
Reason: We have received a lot of great designs, but due to the sheer number we couldn't respond to all. We will extend the deadline for another 7 days to finalize and provide feedback to designers.
Thank you for your hard work!
Industry/Entity Type
Business
Look and feel
Each slider illustrates characteristics of the customer's brand and the style your logo design should communicate.

```html
<!DOCTYPE html>
<html lang="en">
<head>
<meta charset="utf-8">
<title>Norvanta Kitchens – Business Card</title>
<link href="https://fonts.googleapis.com/css2?family=Cinzel:wght@400;600&display=swap" rel="stylesheet">
<style>
  :root {
    --backdrop: #3a342e;
    --card: #141414;
    --card-edge: #2a2a2a;
    --band: #1c1c1c;
    --band-line: #0a0a0a;
    --band-highlight: #262626;
    --gold: #c8b184;
    --muted: #5c5c5c;
    --label: #6b6b6b;
  }
  * { box-sizing: border-box; margin: 0; padding: 0; }
  html, body {
    width: 1200px;
    height: 750px;
    overflow: hidden;
    background: var(--backdrop);
  }
  .canvas {
    position: relative;
    width: 1200px;
    height: 750px;
  }
  .card {
    position: absolute;
    left: 272px;
    width: 589px;
    height: 334px;
    border-radius: 20px;
    background: linear-gradient(180deg, #191919 0%, var(--card) 60%, #111 100%);
    box-shadow: 0 0 0 1px var(--card-edge), 0 6px 14px rgba(0,0,0,0.55);
    overflow: hidden;
    font-family: "Cinzel", serif;
  }
  .card--front { top: 26px; }
  .card--back { top: 377px; }

  .rule {
    position: absolute;
    left: 0;
    width: 100%;
    height: 10px;
    background: var(--band);
    border-top: 2px solid var(--band-line);
    border-bottom: 1px solid var(--band-highlight);
  }
  .card--front .rule, .card--back .rule { top: 92px; }

  .foot-band {
    position: absolute;
    left: 0;
    bottom: 0;
    width: 100%;
    background: linear-gradient(180deg, #1f1f1f 0%, #181818 100%);
    border-top: 2px solid var(--band-line);
    box-shadow: inset 0 1px 0 var(--band-highlight);
  }
  .card--front .foot-band { top: 246px; }
  .card--back .foot-band { top: 240px; }
  .card--back .foot-divider {
    position: absolute;
    left: 0;
    top: 224px;
    width: 100%;
    height: 16px;
    background: #121212;
    border-top: 1px solid var(--band-highlight);
  }

  .brand-name {
    position: absolute;
    left: 0;
    width: 100%;
    top: 178px;
    text-align: center;
    font-weight: 600;
    font-size: 27px;
    letter-spacing: 1px;
    color: var(--gold);
  }

  .person {
    position: absolute;
    left: 0;
    width: 100%;
    top: 128px;
    text-align: center;
  }
  .person__name {
    font-weight: 400;
    font-size: 38px;
    color: var(--gold);
    letter-spacing: 1px;
    line-height: 1;
  }
  .person__role {
    margin-top: 8px;
    font-size: 16px;
    letter-spacing: 5px;
    color: var(--muted);
    text-transform: uppercase;
  }

  .contact {
    position: absolute;
    left: 0;
    width: 100%;
    top: 250px;
    text-align: center;
    font-size: 17px;
    line-height: 21px;
    color: var(--label);
    text-transform: uppercase;
  }
  .contact__sep { margin: 0 14px; }
</style>
</head>
<body>
<main class="canvas">
  <section class="card card--front" aria-label="Card front">
    <div class="rule"></div>
    <p class="brand-name">Norvanta Kitchens</p>
    <div class="foot-band"></div>
  </section>

  <section class="card card--back" aria-label="Card back">
    <div class="rule"></div>
    <div class="person">
      <p class="person__name">Marcus Hale</p>
      <p class="person__role">Director</p>
    </div>
    <div class="foot-divider"></div>
    <div class="foot-band"></div>
    <div class="contact">
      <p>Adress:<span class="contact__sep">|</span>Fax:&nbsp;&nbsp;&nbsp;&nbsp;&nbsp;&nbsp;</p>
      <p>Phone:<span class="contact__sep">|</span>Cell:&nbsp;&nbsp;&nbsp;&nbsp;&nbsp;&nbsp;</p>
      <p>Email:</p>
    </div>
  </section>
</main>
</body>
</html>
```